RM Tomás Ferrier (Business Card)

Hi designers, in this work, I'm looking for an sophisticated stylish, elegant and proffesional personal card. We have a laboratory of pathology automated, with equipments high quality.
In this web the designers, have created my business logo, the name is "RM Tomás Ferrier"
In our lab, we principal work is to prepare the biopsies for further diagnostic of diseases like cancer, tumors, etc.
I need that the first face, only having my complete logo (Rm Tomás Ferrier, Laboratorio de procesamiento Histologico)
The overleaf, could repeat the same logo, like water logo.
In this face, I need to say: My full data:

Técnico en Anatomía Patológica
Tomás Ferrier Bustos M.P 48207
Av. Ramón Quiroga 817 - 2do piso - Instituto Brandeck.
Córdoba, Argentina
(0351) 156284930
ferrier.tomas@correoluz.com

with respect the colors of card, use your imagination, the original logo color is violet, I haven't chosen a color base for the card.

attached pictures are examples of cards I like your DESIGN.
Attached too, the original logo to my company.

the size of card are:
horizontal: 9cm
vertical: 5,5cm

any question that you have, not doubt to question me,
Hand to work!

Industry/Entity Type

Laboratory

Requirements
Must have
• designers sophisticated, not simples, like show the images attached

```html
<!DOCTYPE html>
<html lang="es">
<head>
<meta charset="utf-8">
<title>Tomás Ferrier — Papelería</title>
<link rel="stylesheet" href="https://fonts.googleapis.com/css2?family=Roboto+Condensed:wght@400;700&family=Roboto:wght@300;400&display=swap">
<style>
  :root {
    --violet: #4a2475;
    --violet-dark: #321552;
    --silver: #a9a9ad;
    --silver-light: #d6d6da;
    --paper: #f4f4f5;
    --paper-edge: #e4e4e6;
    --ink: #55555a;
    --ink-soft: #8a8a90;
    --backdrop: #2d2622;
  }
  * { box-sizing: border-box; margin: 0; padding: 0; }
  html, body { width: 1200px; height: 900px; overflow: hidden; }
  body {
    position: relative;
    background: var(--backdrop);
    font-family: "Roboto", Arial, sans-serif;
    color: var(--ink);
  }
  .sheet {
    position: absolute;
    overflow: hidden;
    background: radial-gradient(ellipse at 45% 30%, #ffffff 0%, var(--paper) 55%, var(--paper-edge) 100%);
    box-shadow: 0 10px 28px rgba(0,0,0,.55);
  }
  .card { border-radius: 10px; }
  .card-large { border-radius: 2px; }

  /* brand lockup */
  .brand { position: absolute; left: 0; right: 0; text-align: center; z-index: 3; }
  .brand-mark {
    display: inline-block; border-radius: 50%;
    border: 2px solid var(--violet); vertical-align: middle;
  }
  .brand-name {
    font-family: "Roboto Condensed", Arial, sans-serif;
    font-weight: 400; color: var(--violet);
    letter-spacing: .22em; text-transform: uppercase;
    vertical-align: middle; margin-left: 6px;
  }
  .brand-tagline {
    display: block; margin-top: 3px;
    font-family: "Roboto Condensed", Arial, sans-serif; font-weight: 700;
    color: var(--ink); text-transform: uppercase; letter-spacing: -.01em;
    border-top: 1px solid var(--ink-soft); padding-top: 2px;
    width: max-content; margin-left: auto; margin-right: auto;
  }
  .watermark {
    position: absolute;
    font-family: "Roboto Condensed", Arial, sans-serif; font-weight: 400;
    color: rgba(90, 80, 110, .08); white-space: nowrap; letter-spacing: .05em;
  }
  .wave { position: absolute; left: 0; bottom: 0; width: 100%; display: block; }
  .contact { position: absolute; font-size: 10px; color: var(--ink); line-height: 1.6; white-space: nowrap; z-index: 3; }
  .contact svg { width: 9px; height: 9px; vertical-align: -1px; margin-right: 4px; }

  /* letterhead */
  .letterhead { left: 110px; top: 40px; width: 560px; height: 800px; }
  .letterhead .brand { top: 24px; }
  .letterhead .brand-mark { width: 26px; height: 26px; }
  .letterhead .brand-name { font-size: 13px; }
  .letterhead .brand-tagline { font-size: 12px; }
  .letterhead-rule { position: absolute; left: 14px; right: 14px; top: 106px; height: 1px; background: var(--ink-soft); }
  .letterhead .watermark { left: 40px; bottom: 200px; font-size: 64px; }
  .letterhead .contact-reach { left: 150px; bottom: 132px; font-size: 11px; }
  .letterhead .contact-address { left: 330px; bottom: 150px; font-size: 10.5px; }

  /* large card */
  .card-large { left: 600px; top: 140px; width: 440px; height: 260px; }
  .card-large .brand { top: 22px; left: 30px; right: auto; text-align: left; }
  .card-large .brand-mark { width: 26px; height: 26px; }
  .card-large .brand-name { font-size: 13px; }
  .card-large .brand-tagline { font-size: 12px; margin-left: 0; }
  .card-large .watermark { left: 30px; top: 96px; font-size: 34px; }
  .card-large .contact-address { right: 30px; top: 128px; text-align: right; font-size: 9px; }
  .card-large .contact-reach { right: 30px; top: 156px; font-size: 9px; }
  .card-large .contact-reach span + span { margin-left: 8px; }

  /* small cards */
  .card-front { left: 800px; top: 430px; width: 270px; height: 168px; }
  .card-back { left: 810px; top: 615px; width: 266px; height: 165px; }
  .card-small .brand { top: 16px; }
  .card-small .brand-mark { width: 20px; height: 20px; }
  .card-small .brand-name { font-size: 10px; }
  .card-small .brand-tagline { font-size: 9px; }
  .card-front .watermark { left: 90px; bottom: 16px; font-size: 22px; color: rgba(255,255,255,.09); z-index: 2; }
  .card-back .brand-address { position: absolute; top: 66px; left: 0; right: 0; text-align: center; font-size: 5.5px; color: var(--ink-soft); line-height: 1.4; }
  .holder { position: absolute; left: 16px; top: 96px; }
  .holder-name { font-size: 10px; color: var(--ink); font-weight: 300; }
  .holder-title, .holder-license { font-size: 6.5px; color: var(--violet); line-height: 1.5; }
  .card-back .divider { position: absolute; left: 150px; top: 94px; width: 1px; height: 34px; background: var(--violet); }
  .card-back .contact-reach { left: 158px; top: 95px; font-size: 6px; color: var(--ink-soft); }
  .card-back .contact-reach svg { width: 6px; height: 6px; }
</style>
</head>
<body>

<svg width="0" height="0" style="position:absolute" aria-hidden="true">
  <symbol id="icon-phone" viewBox="0 0 10 10"><rect x="2.5" y="0.5" width="5" height="9" rx="1" fill="none" stroke="#555" stroke-width="1"/><circle cx="5" cy="8" r=".6" fill="#555"/></symbol>
  <symbol id="icon-mail" viewBox="0 0 10 10"><rect x="0.5" y="0.5" width="9" height="9" rx="1.5" fill="#555"/><path d="M2 3.5 L5 5.8 L8 3.5" fill="none" stroke="#fff" stroke-width="1"/></symbol>
</svg>

<!-- Letterhead -->
<section class="sheet letterhead">
  <div class="brand">
    <span class="brand-mark"></span><span class="brand-name">Tomás Ferrier</span>
    <span class="brand-tagline">Laboratorio de Procesamiento Histologico</span>
  </div>
  <div class="letterhead-rule"></div>
  <div class="watermark">Tomás Ferrier</div>
  <div class="contact contact-reach">
    <div><svg><use href="#icon-phone"/></svg>(0351) 156284930</div>
    <div><svg><use href="#icon-mail"/></svg>ferrier.tomas@correoluz.com</div>
  </div>
  <div class="contact contact-address">
    <div>Av. Ramón Quiroga 817 - 2do piso - Instituto</div>
    <div>Brandeck, Córdoba, Argentina</div>
  </div>
  <svg class="wave" viewBox="0 0 560 120" height="120" preserveAspectRatio="none" aria-hidden="true">
    <path d="M0 34 Q200 95 560 8 L560 24 Q200 108 0 50 Z" fill="var(--silver-light)"/>
    <path d="M0 43 Q200 102 560 19" fill="none" stroke="var(--silver)" stroke-width="3"/>
    <path d="M0 62 Q200 116 560 34 L560 120 L0 120 Z" fill="var(--violet)"/>
  </svg>
</section>

<!-- Large card -->
<section class="sheet card card-large">
  <div class="brand">
    <span class="brand-mark"></span><span class="brand-name">Tomás Ferrier</span>
    <span class="brand-tagline">Laboratorio de Procesamiento Histologico</span>
  </div>
  <div class="watermark">Tomás Ferrier</div>
  <div class="contact contact-address">
    <div>Av. Ramón Quiroga 817 - 2do piso - Instituto</div>
    <div>Brandeck, Córdoba, Argentina</div>
  </div>
  <div class="contact contact-reach">
    <span><svg><use href="#icon-phone"/></svg>(0351) 156284930</span><span><svg><use href="#icon-mail"/></svg>ferrier.tomas@correoluz.com</span>
  </div>
  <svg class="wave" viewBox="0 0 440 90" height="90" preserveAspectRatio="none" aria-hidden="true">
    <path d="M0 8 Q220 60 440 0 L440 14 Q220 72 0 22 Z" fill="var(--silver-light)"/>
    <path d="M0 18 Q220 70 440 8" fill="none" stroke="var(--silver)" stroke-width="2.5"/>
    <path d="M0 30 Q220 85 440 20 L440 90 L0 90 Z" fill="var(--violet)"/>
  </svg>
</section>

<!-- Small card, front -->
<section class="sheet card card-small card-front">
  <div class="brand">
    <span class="brand-mark"></span><span class="brand-name">Tomás Ferrier</span>
    <span class="brand-tagline">Laboratorio de Procesamiento Histologico</span>
  </div>
  <svg class="wave" viewBox="0 0 270 80" height="80" preserveAspectRatio="none" aria-hidden="true">
    <path d="M0 24 Q135 -4 270 10 L270 18 Q135 4 0 34 Z" fill="var(--silver-light)"/>
    <path d="M0 30 Q135 6 270 20 L270 80 L0 80 Z" fill="var(--violet)"/>
  </svg>
  <div class="watermark">Tomás Ferrier</div>
</section>

<!-- Small card, back -->
<section class="sheet card card-small card-back">
  <div class="brand">
    <span class="brand-mark"></span><span class="brand-name">Tomás Ferrier</span>
    <span class="brand-tagline">Laboratorio de Procesamiento Histologico</span>
  </div>
  <div class="brand-address">Av. Ramón Quiroga 817 - 2do piso - Instituto Brandeck<br>Córdoba, Argentina</div>
  <div class="holder">
    <div class="holder-name">Tomás Ferrier Bustos</div>
    <div class="holder-title">Técnico en Anatomía Patológica</div>
    <div class="holder-license">M.P 48207</div>
  </div>
  <div class="divider"></div>
  <div class="contact contact-reach">
    <div><svg><use href="#icon-phone"/></svg>(0351) 156284930</div>
    <div><svg><use href="#icon-mail"/></svg>ferrier.tomas@correoluz.com</div>
  </div>
  <svg class="wave" viewBox="0 0 266 22" height="22" preserveAspectRatio="none" aria-hidden="true">
    <path d="M0 22 Q133 2 266 6 L266 22 Z" fill="var(--violet)"/>
  </svg>
</section>

</body>
</html>
```